Postcard Design

Postcard for the following:

Front of postcard:
A new little beauty and health haven has opened up just around the corner at 42 Marston Lane, Fernwood Rise.
Just like you, Mabel’s Lantern is special, offering treatments and services tailor made to your specific needs. Mabel has over 24 years of industry experience and offers a unique approach to helping you feel healthful, nourished and happy. Her treatments are brilliantly effective and include remedial massage therapies and reflexology, gorgeous rejuvenating facials and much much more…………..come and experience this unique and 100% organic little piece of heaven.
You deserve to feel great so we work from the inside out by offering nutritional health advice and formulations developed especially for you. We wholly nourish the individual in the wise woman tradition of healing and happiness.
As a special welcome gift I would like to offer you $15 off any service
By appointment 027 5162930 I look forward to seeing you soon

Back of postcard:
The hearth has been the centre of human life for at least 400,000 years. it is the place where people meet to cook, eat, talk together and heal. The ' hearth' was the heart of the home It was the centre of activity, where everyone gathered to keep warm, laugh, listen to the stories of old and heal. It was the place of physical and emotional nourishment. The hearth is a symbol for the hospitality and living spirit of the home.

Industry/Entity Type

Hospitality

Requirements
Nice to have
• A logo for the business would be really good.

```html
<!DOCTYPE html>
<html lang="en">
<head>
<meta charset="utf-8">
<title>Mabel’s Lantern Postcard</title>
<link href="https://fonts.googleapis.com/css2?family=Bebas+Neue&family=Cormorant+Garamond:wght@600&family=Lato:wght@400;700&display=swap" rel="stylesheet">
<style>
:root{
  --stage:#2e2e2e;
  --paper:#ffffff;
  --navy:#2456a8;
  --sky:#2aa9e0;
  --ink:#3d3d3d;
  --photo-skin:#e9d3c6;
  --photo-light:#f3ece8;
}
*{box-sizing:border-box;margin:0;padding:0}
html,body{width:806px;height:1200px;overflow:hidden}
body{background:var(--stage);position:relative;font-family:'Lato',sans-serif}

.card{position:absolute;background:var(--paper);overflow:hidden;box-shadow:0 4px 14px rgba(0,0,0,.4)}
.card-front{left:72px;top:40px;width:652px;height:506px}
.card-back{left:76px;top:628px;width:640px;height:506px}

.photo{position:absolute;background:linear-gradient(135deg,var(--photo-light),var(--photo-skin))}
.photo-1{left:6px;top:0;width:206px;height:164px}
.photo-2{left:6px;top:172px;width:206px;height:164px}
.photo-3{left:6px;top:344px;width:206px;height:162px}

.brand{position:absolute;left:218px;top:14px;width:434px;text-align:center;font-family:'Bebas Neue',sans-serif;font-size:54px;letter-spacing:1px;color:var(--navy);line-height:1}
.tagline{position:absolute;left:230px;top:74px;width:410px;text-align:center;font-family:'Cormorant Garamond',serif;font-weight:600;font-size:19px;line-height:1.15;color:var(--navy)}
.intro{position:absolute;left:228px;top:140px;width:416px;font-size:12.6px;line-height:1.35;color:var(--ink)}

.panel-treatments{position:absolute;left:218px;top:214px;width:434px;height:126px;background:var(--sky);border-radius:26px 0 0 0}
.panel-treatments p{position:absolute;left:14px;top:10px;width:254px;color:#fff;font-size:13.4px;line-height:1.3}
.offer{position:absolute;left:482px;top:206px;width:146px;height:146px;border-radius:50%;background:#fff;border:10px solid var(--navy);box-shadow:0 0 0 4px #fff inset;display:flex;align-items:center;justify-content:center;text-align:center;font-weight:700;font-size:12.4px;line-height:1.15;color:var(--ink)}
.offer strong{font-size:20px;color:var(--navy)}

.panel-nourish{position:absolute;left:218px;top:350px;width:434px;height:156px;background:var(--navy)}
.panel-nourish p{position:absolute;left:14px;top:24px;width:400px;color:#fff;font-size:13.4px;line-height:1.3}
.appointment{position:absolute;left:12px;top:102px;width:388px;height:26px;border-radius:13px;background:var(--sky);color:#fff;font-weight:700;font-size:12.4px;line-height:26px;padding-left:12px}

.back-panel{position:absolute;left:0;top:0}
.back-heading{position:absolute;left:8px;top:28px;width:228px;height:40px;background:#fff;border-radius:0 20px 20px 0;font-family:'Bebas Neue',sans-serif;font-size:27px;color:var(--navy);line-height:42px;padding-left:10px;letter-spacing:.5px}
.back-text{position:absolute;left:16px;top:90px;width:290px;color:#fff;font-size:10.4px;line-height:1.68}
.back-text strong{font-size:15px}
.thumb{position:absolute;top:258px;width:136px;height:110px;background:var(--navy);padding:8px}
.thumb span{display:block;width:100%;height:100%}
.thumb-oil{left:16px}
.thumb-oil span{background:linear-gradient(135deg,#f4eef1,#c99ac0)}
.thumb-foot{left:166px}
.thumb-foot span{background:linear-gradient(135deg,#f1ddd0,#d9a88e)}
.contact{position:absolute;left:28px;color:#fff;font-weight:700;display:flex;align-items:center;gap:6px}
.contact-phone{top:422px;font-size:25px}
.contact-web{top:452px;font-size:19px}

.stamp{position:absolute;left:524px;top:48px;width:78px;height:78px;border:1.5px solid #222}
.address-line{position:absolute;left:344px;width:262px;height:1px;background:#555}
.photo-spa{position:absolute;left:390px;top:250px;width:250px;height:256px;background:radial-gradient(circle at 65% 45%,#e6ecef,#f7f6f3 55%,#fff 80%)}
</style>
</head>
<body>

<section class="card card-front">
  <div class="photo photo-1" role="img" aria-label="Woman relaxing with a crystal on her forehead"></div>
  <div class="photo photo-2" role="img" aria-label="Woman receiving a facial massage"></div>
  <div class="photo photo-3" role="img" aria-label="Hot stone massage on a woman’s back"></div>

  <h1 class="brand">Mabel’s Lantern</h1>
  <p class="tagline">A new little beauty and health haven has opened up just around the corner at 42 Marston Lane, Fernwood Rise.</p>
  <p class="intro">Mabel’s Lantern is special, offering treatments and services tailor made to your specific needs. Mabel has over 24 years of industry experience and offers a unique approach to helping you feel healthful, nourished and happy.</p>

  <div class="panel-treatments">
    <p>Her treatments are brilliantly effective and include remedial massage therapies and reflexology, gorgeous rejuvenating facials and much much more………… come and experience this unique and 100% organic little piece of heaven.</p>
  </div>
  <div class="offer"><div>As a special<br>welcome gift I<br>would like to<br>offer you <strong>$15</strong><br>off any service</div></div>

  <div class="panel-nourish">
    <p>We work from the inside out by offering nutritional health advice and formulations developed especially for you. We wholly nourish the individual in the wise woman tradition of healing and happiness.</p>
    <div class="appointment">By appointment 0275162930&nbsp; I look forward to seeing you soon</div>
  </div>
</section>

<section class="card card-back">
  <svg class="back-panel" width="330" height="506" viewBox="0 0 330 506">
    <path d="M0 0H296a30 30 0 0 1 30 30V388H0Z" fill="var(--sky)"/>
    <path d="M0 372Q0 396 30 396H326V482a24 24 0 0 1-24 24H0Z" fill="var(--navy)"/>
    <path d="M0 360Q0 386 30 386H326V396H30Q0 396 0 372Z" fill="#fff"/>
  </svg>
  <h2 class="back-heading">What is a Hearth …</h2>
  <p class="back-text">The hearth has been the centre of human life for at least <strong>400,000</strong> years. it is the place where people meet to cook, eat and talk together and heal. The ' hearth' was the heart of the home It was the centre of activity, where everyone gathered to eat and cook, to sit and warm themselves, and listen to the stories of old. It was the place of physical and emotional nourishment hearth is a symbol for the hospitality and living spirit of the home.</p>
  <div class="thumb thumb-oil"><span role="img" aria-label="Essential oil bottle with orchid petals"></span></div>
  <div class="thumb thumb-foot"><span role="img" aria-label="Hands giving a foot reflexology massage"></span></div>

  <div class="contact contact-phone">
    <svg width="20" height="22" viewBox="0 0 20 22"><rect x="1" y="1" width="18" height="20" rx="4" fill="none" stroke="#fff" stroke-width="2"/><path d="M7 5c-1 1-1 3 0 6s3 5 5 6l2-2-2-2-1 1c-1-1-2-2-2-4l1-1-2-2z" fill="#fff"/></svg>
    000-000-000
  </div>
  <div class="contact contact-web">
    <svg width="20" height="14" viewBox="0 0 20 14"><rect x="1" y="1" width="18" height="12" fill="none" stroke="#fff" stroke-width="2"/><path d="M1 1l9 7 9-7" fill="none" stroke="#fff" stroke-width="2"/></svg>
    www.mabelslantern.co.nz
  </div>

  <div class="stamp"></div>
  <div class="address-line" style="top:157px"></div>
  <div class="address-line" style="top:190px"></div>
  <div class="address-line" style="top:223px"></div>
  <div class="photo-spa" role="img" aria-label="Bowl of bath salts with spa stones and oil"></div>
</section>

</body>
</html>
```